Logo for KEX Co. roofing company
KEX, Co.
Professional
Dalmon Fitch
Owner
17 Hollet Lane Walpole, MA 02974
Estimates
kexcoroofing@brightpost.net
kexcoroofing.net
Fully Insured
I want long used as the focus point. Company colors: Primary- Green, secondary- Black and yellow. on the back of the card I want kexcoroofing.net to be centered
brambeek brambeek
Please upload your logo Ai file.. thanks
Fitch42 Fitch42
I already have a logo that was previously made for me, I would like for that logo to be used.

```html
<!DOCTYPE html>
<html lang="en">
<head>
<meta charset="UTF-8">
<title>KEX Co. Business Card</title>
<link rel="stylesheet" href="https://fonts.googleapis.com/css2?family=Open+Sans:wght@400;600&family=Cinzel:wght@500&display=swap">
<style>
  :root {
    --backdrop: #e9e7e3;
    --card-dark: #2e2e30;
    --card-light: #ffffff;
    --brand-green: #2b9a3a;
    --brand-black: #2a2a2a;
    --rule-grey: #b9b9b9;
    --text-grey: #5a5a5a;
    --text-light: #d8d8d8;
  }
  html, body {
    margin: 0;
    width: 1200px;
    height: 904px;
    overflow: hidden;
    background: var(--backdrop);
    font-family: "Open Sans", Arial, sans-serif;
  }
  .card {
    position: absolute;
    width: 640px;
    height: 366px;
    border-radius: 26px;
    overflow: hidden;
    box-shadow: 0 6px 18px rgba(0,0,0,0.18);
  }
  .card-back {
    left: 110px;
    top: 70px;
    background: var(--card-dark);
    display: flex;
    align-items: center;
    justify-content: center;
  }
  .card-back .website {
    color: var(--text-light);
    font-size: 15px;
    letter-spacing: 0.5px;
  }
  .card-front {
    left: 450px;
    top: 468px;
    background: var(--card-light);
  }
  .card-front .waves {
    position: absolute;
    inset: 0;
  }
  .brand {
    position: absolute;
    left: 44px;
    top: 96px;
    display: flex;
    align-items: center;
    gap: 12px;
  }
  .brand-mark {
    width: 16px;
    height: 16px;
    background: var(--brand-green);
  }
  .brand-name {
    font-family: "Cinzel", Georgia, serif;
    font-weight: 500;
    font-size: 46px;
    color: var(--text-grey);
    line-height: 1;
  }
  .contact {
    position: absolute;
    left: 368px;
    top: 58px;
  }
  .contact .name {
    color: var(--brand-green);
    font-weight: 600;
    font-size: 19px;
    margin: 0;
    line-height: 1.2;
  }
  .contact .role {
    color: var(--text-grey);
    font-size: 12px;
    margin: 0 0 8px;
  }
  .contact ul {
    list-style: none;
    margin: 0;
    padding: 0;
  }
  .contact li {
    display: flex;
    align-items: center;
    gap: 8px;
    color: var(--text-grey);
    font-size: 13px;
    line-height: 19px;
  }
  .contact li svg { width: 11px; height: 11px; fill: var(--brand-green); flex: none; }
  .address {
    position: absolute;
    left: 44px;
    top: 222px;
    color: var(--text-grey);
    font-size: 13px;
    line-height: 18px;
  }
  .front-website {
    position: absolute;
    left: 452px;
    top: 302px;
    display: flex;
    align-items: center;
    gap: 7px;
    color: #ffffff;
    font-size: 13px;
  }
  .front-website svg { width: 11px; height: 11px; fill: #ffffff; }
</style>
</head>
<body>

<section class="card card-back">
  <span class="website">www.kexcoroofing.net</span>
</section>

<section class="card card-front">
  <svg class="waves" viewBox="0 0 640 366" preserveAspectRatio="none" aria-hidden="true">
    <path d="M0,276 C200,318 430,256 640,200" fill="none" stroke="var(--rule-grey)" stroke-width="2"/>
    <path d="M0,285 C200,330 430,265 640,210 L640,232 C430,288 210,345 0,305 Z" fill="var(--brand-black)"/>
    <path d="M0,318 C210,352 440,295 640,242 L640,366 L0,366 Z" fill="var(--brand-green)"/>
  </svg>

  <div class="brand">
    <span class="brand-mark"></span>
    <span class="brand-name">KEX Co.</span>
  </div>

  <div class="contact">
    <p class="name">Dalmon Fitch</p>
    <p class="role">Owner</p>
    <ul>
      <li><svg viewBox="0 0 12 12"><path d="M2.5 1 L4.5 1 L5.5 3.5 L4.2 4.5 C4.9 6 6 7.1 7.5 7.8 L8.5 6.5 L11 7.5 L11 9.5 C11 10.3 10.3 11 9.5 11 C5 11 1 7 1 2.5 C1 1.7 1.7 1 2.5 1 Z"/></svg>617-555-0142</li>
      <li><svg viewBox="0 0 12 12"><path d="M2.5 1 L4.5 1 L5.5 3.5 L4.2 4.5 C4.9 6 6 7.1 7.5 7.8 L8.5 6.5 L11 7.5 L11 9.5 C11 10.3 10.3 11 9.5 11 C5 11 1 7 1 2.5 C1 1.7 1.7 1 2.5 1 Z"/></svg>617-555-0187</li>
      <li><svg viewBox="0 0 12 12"><rect x="2.5" y="0.5" width="7" height="11" rx="1.2"/></svg>781-555-0163</li>
      <li><svg viewBox="0 0 12 12"><path d="M0.5 2 H11.5 V10 H0.5 Z M1.2 2.6 L6 6.4 L10.8 2.6" stroke="#fff" stroke-width="0.8"/></svg>kexcoroofing@brightpost.net</li>
    </ul>
  </div>

  <div class="address">
    17 Hollet Lane<br>
    Walpole, MA 02974
  </div>

  <div class="front-website">
    <svg viewBox="0 0 12 12"><circle cx="6" cy="6" r="5.5"/></svg>
    www.kexcoroofing.net
  </div>
</section>

</body>
</html>
```